COVID-19 Related Signage for Hotel

Need to create new COVID-19 related signage utilizing our brand assets. Please use screenshots for copy/direction. essentially duplicate the screenshots but with our logo/branding.

All brand assets have been uploaded and examples of signage content. Pictures are not necessary but you can add them if you want similar to the examples attached.

Sign requirements

sign 1. Text "Hand Sanitizer Station" can add graphic
sign 2. Text "Protect Yourself" duplicate copy in the attached pictures
sign 3. Text "Face Mask Required" can add graphic
sign 4. Text "Face Covering Do's and Don'ts with text from "Face-covering checklist.jpg" REMOVE BWT logo or website or 3 face mask graphics
sign 5. Text "Maintain 6 Foot Distance" This sign will be printed and placed on the ground for guests to know where to stand in queue. Would prefer a circular Design. sign 6. Text "Wet, Lather, Scrub, Rinse, Dry" similar to screenshots attached.

ALL signs should have same look and feel throughout utilizing our brand graphics, logo, colors, and guidelines.

Target Market(s)

Hotel Guests

Industry/Entity Type

Hotel

Font styles to use
Sans Serif

Requirements
Must have
• Cohesive, unified branding look and feel

Should not have
• any use of the word "COVID-19" or Coronavirus.

```html
<!DOCTYPE html>
<html lang="en">
<head>
<meta charset="utf-8">
<title>Guest Health Signage – Pine Hollow Inn</title>
<link href="https://fonts.googleapis.com/css2?family=Oswald:wght@300;400;500&display=swap" rel="stylesheet">
<style>
  :root{
    --orange:#f48a33;
    --charcoal:#5b5b5d;
    --ink:#4a4a4c;
    --paper:#f7f7f7;
    --stage:#d9d9d9;
    --white:#ffffff;
    --tick:#3aa14a;
    --cross:#e0262b;
  }
  *{box-sizing:border-box;margin:0;padding:0}
  html,body{width:1200px;height:1059px;overflow:hidden}
  body{background:var(--stage);font-family:'Oswald',sans-serif;position:relative;color:var(--ink)}
  .sign{position:absolute;width:445px;height:222px;background:var(--paper);overflow:hidden}
  .sign::after{content:"";position:absolute;left:0;right:0;bottom:0;height:9px;background:var(--orange)}
  .brand{position:absolute;border-radius:50%;background:var(--orange);color:var(--white);
    display:flex;align-items:center;justify-content:center;font-weight:300;font-size:13px;line-height:1;text-align:center}
  .headline{position:absolute;left:24px;font-weight:400;color:var(--ink);letter-spacing:-0.5px}

  /* face covering */
  .covering{left:136px;top:173px;background:var(--white)}
  .covering .headline{top:14px;font-size:50px;line-height:54px}
  .covering .brand{left:354px;top:16px;width:72px;height:72px}
  .tab{position:absolute;top:129px;width:143px;height:18px;background:var(--orange);color:var(--white);
    font-size:16px;line-height:18px;padding-left:6px}
  .tab.do{left:22px}.tab.dont{left:208px}
  .tab-arrows{position:absolute;left:177px;top:132px}
  .rule-list{position:absolute;top:155px;list-style:none;font-size:7.5px;font-weight:300;line-height:13px;color:var(--ink)}
  .rule-list.do{left:24px}.rule-list.dont{left:214px}
  .rule-list li{position:relative;padding-left:14px}
  .rule-list li.cont{padding-left:14px}
  .rule-list .mark{position:absolute;left:0;top:3px}

  /* floor decals */
  .floor{position:absolute;top:182px;width:204px;height:204px}
  .floor.a{left:612px}.floor.b{left:833px}

  /* sanitizer */
  .sanitize{left:136px;top:423px}
  .sanitize .headline{top:12px;font-size:60px;line-height:62px}
  .sanitize .brand{left:356px;top:11px;width:72px;height:72px}
  .art-circle{position:absolute;border-radius:50%;background:var(--orange);box-shadow:0 0 0 2px var(--white),0 0 0 3.5px var(--orange)}
  .sanitize .art-circle{left:236px;top:59px;width:134px;height:134px}

  /* hand washing steps */
  .steps{left:602px;top:423px}
  .steps::after{display:none}
  .steps .brand{left:356px;top:12px;width:72px;height:72px}
  .step{position:absolute;bottom:0;width:89px;padding:8px 8px 0 9px;color:var(--white);font-weight:300;font-size:14px;line-height:16px}
  .step.o{background:var(--orange)}.step.g{background:var(--charcoal)}
  .step-title{position:absolute;font-size:33px;font-weight:400;line-height:1;letter-spacing:-0.5px}
  .step-title.o{color:var(--orange)}.step-title.g{color:var(--ink)}

  /* protect yourself */
  .protect{left:137px;top:665px}
  .protect .headline{top:14px;font-size:54px;line-height:54px}
  .protect .brand{left:354px;top:15px;width:72px;height:72px}
  .protect-band{position:absolute;left:0;right:0;top:157px;height:56px;background:var(--charcoal)}
  .tip{position:absolute;top:133px;width:86px;text-align:center;color:var(--white);font-size:10px;line-height:12px;font-weight:300}
  .tip .ico{display:block;margin:0 auto 7px;width:46px;height:46px;border-radius:50%;background:var(--orange);box-shadow:0 0 0 1.5px var(--white),0 0 0 3px var(--orange)}

  /* face mask */
  .mask{left:602px;top:665px}
  .mask .headline{top:8px;font-size:62px;line-height:63px}
  .mask .brand{left:345px;top:22px;width:78px;height:78px;font-size:14px}
  .mask .art-circle{left:220px;top:68px;width:132px;height:132px}
</style>
</head>
<body>

<!-- Face Covering Do's and Don'ts -->
<section class="sign covering">
  <h2 class="headline">Face Covering<br>Do’s and Don’ts:</h2>
  <div class="brand">pine hollow inn</div>
  <div class="tab do">Do:</div>
  <svg class="tab-arrows" width="22" height="12" viewBox="0 0 22 12" aria-hidden="true">
    <g fill="var(--orange)"><path d="M0 1l5 5-5 5z"/><path d="M8 1l5 5-5 5z"/><path d="M16 1l5 5-5 5z"/></g>
  </svg>
  <div class="tab dont">Don’t:</div>
  <ul class="rule-list do">
    <li><svg class="mark" width="10" height="7" viewBox="0 0 10 7"><path d="M1 3.5l3 2.5L9 1" fill="none" stroke="var(--tick)" stroke-width="1.3"/></svg>Make sure you can breathe through it</li>
    <li><svg class="mark" width="10" height="7" viewBox="0 0 10 7"><path d="M1 3.5l3 2.5L9 1" fill="none" stroke="var(--tick)" stroke-width="1.3"/></svg>Wear it whenever going out in public</li>
    <li><svg class="mark" width="10" height="7" viewBox="0 0 10 7"><path d="M1 3.5l3 2.5L9 1" fill="none" stroke="var(--tick)" stroke-width="1.3"/></svg>Make sure it covers your nose and mouth</li>
    <li class="cont">wash after using</li>
  </ul>
  <ul class="rule-list dont">
    <li><svg class="mark" width="8" height="8" viewBox="0 0 8 8"><path d="M1 1l6 6M7 1L1 7" stroke="var(--cross)" stroke-width="1.3"/></svg>Use if under two years old</li>
    <li><svg class="mark" width="8" height="8" viewBox="0 0 8 8"><path d="M1 1l6 6M7 1L1 7" stroke="var(--cross)" stroke-width="1.3"/></svg>Use surgical masks or other PPE intended</li>
    <li class="cont">for healthcare workers</li>
  </ul>
</section>

<!-- Floor decals -->
<svg class="floor a" viewBox="0 0 204 204" role="img" aria-label="Maintain 6 foot distance floor decal">
  <defs>
    <path id="arcTop" d="M32 102a70 70 0 0 1 140 0"/>
    <path id="arcBot" d="M22 102a80 80 0 0 0 160 0"/>
  </defs>
  <circle cx="102" cy="102" r="101" fill="var(--orange)"/>
  <circle cx="102" cy="102" r="98" fill="none" stroke="var(--white)" stroke-width="1.2"/>
  <circle cx="102" cy="102" r="70" fill="none" stroke="var(--white)" stroke-width="1.2"/>
  <text font-family="Oswald,sans-serif" font-size="25" font-weight="500" fill="var(--white)" letter-spacing="6"><textPath href="#arcTop" startOffset="50%" text-anchor="middle" dy="-6">MAINTAIN</textPath></text>
  <text font-family="Oswald,sans-serif" font-size="25" font-weight="500" fill="var(--white)" letter-spacing="3"><textPath href="#arcBot" startOffset="50%" text-anchor="middle" side="left">FOOT DISTANCE</textPath></text>
  <text x="102" y="148" text-anchor="middle" font-family="Oswald,sans-serif" font-size="128" font-weight="500" fill="var(--white)">6</text>
  <g fill="var(--white)"><path d="M8 95l6 5-6 5z"/><path d="M17 95l6 5-6 5z"/><path d="M26 95l6 5-6 5z"/></g>
  <circle cx="170" cy="100" r="18" fill="var(--orange)" stroke="var(--white)" stroke-width="1"/>
  <text x="170" y="103" text-anchor="middle" font-family="Oswald,sans-serif" font-size="6.5" font-weight="300" fill="var(--white)">pine hollow</text>
</svg>
<svg class="floor b" viewBox="0 0 204 204" role="img" aria-label="Maintain 6 foot distance floor decal">
  <circle cx="102" cy="102" r="101" fill="var(--orange)"/>
  <circle cx="102" cy="102" r="98" fill="none" stroke="var(--white)" stroke-width="1.2"/>
  <circle cx="102" cy="102" r="70" fill="none" stroke="var(--white)" stroke-width="1.2"/>
  <text font-family="Oswald,sans-serif" font-size="25" font-weight="500" fill="var(--white)" letter-spacing="6"><textPath href="#arcTop" startOffset="50%" text-anchor="middle">MAINTAIN</textPath></text>
  <text font-family="Oswald,sans-serif" font-size="25" font-weight="500" fill="var(--white)" letter-spacing="3"><textPath href="#arcBot" startOffset="50%" text-anchor="middle" side="left">FOOT DISTANCE</textPath></text>
  <text x="102" y="148" text-anchor="middle" font-family="Oswald,sans-serif" font-size="128" font-weight="500" fill="var(--white)">6</text>
  <g fill="var(--white)"><path d="M8 95l6 5-6 5z"/><path d="M17 95l6 5-6 5z"/><path d="M26 95l6 5-6 5z"/></g>
  <circle cx="170" cy="100" r="18" fill="var(--orange)" stroke="var(--white)" stroke-width="1"/>
  <text x="170" y="103" text-anchor="middle" font-family="Oswald,sans-serif" font-size="6.5" font-weight="300" fill="var(--white)">pine hollow</text>
</svg>

<!-- Hand Sanitizing Station -->
<section class="sign sanitize">
  <h2 class="headline">Hand<br>Sanitizing<br>Station</h2>
  <div class="art-circle" role="img" aria-label="Illustration of a hand under a sanitizer pump bottle"></div>
  <div class="brand">pine hollow inn</div>
</section>

<!-- Hand washing steps -->
<section class="sign steps">
  <div class="brand">pine hollow inn</div>
  <span class="step-title o" style="left:18px;top:6px">WET</span>
  <div class="step o" style="left:0;height:181px">Wash with clean, running water</div>
  <span class="step-title g" style="left:91px;top:37px">LATHER</span>
  <div class="step g" style="left:89px;height:150px">Lather with soap, in between fingers, under nails &amp; all over hands</div>
  <span class="step-title o" style="left:184px;top:67px">SCRUB</span>
  <div class="step o" style="left:178px;height:120px">Scrub for at least 20 seconds</div>
  <span class="step-title g" style="left:278px;top:97px">RINSE</span>
  <div class="step g" style="left:267px;height:90px">Rinse with clean, running water</div>
  <span class="step-title o" style="left:375px;top:126px">DRY</span>
  <div class="step o" style="left:356px;height:62px">Dry with a clean towel or air dry</div>
</section>

<!-- Protect Yourself -->
<section class="sign protect">
  <h2 class="headline">Protect<br>Yourself</h2>
  <div class="brand">pine hollow inn</div>
  <div class="protect-band"></div>
  <div class="tip" style="left:12px"><span class="ico" role="img" aria-label="House icon"></span>Stay home if<br>you’re feeling sick</div>
  <div class="tip" style="left:96px"><span class="ico" role="img" aria-label="Masked head icon"></span>Cover your<br>mouth</div>
  <div class="tip" style="left:181px"><span class="ico" role="img" aria-label="Washing hands icon"></span>Wash your hands<br>for at least 20 seconds</div>
  <div class="tip" style="left:266px"><span class="ico" role="img" aria-label="Two people apart icon"></span>Keep distance<br>(6-ft)</div>
  <div class="tip" style="left:350px"><span class="ico" role="img" aria-label="Cleaning surface icon"></span>Clean surfaces<br>regularly</div>
</section>

<!-- Face Mask Required -->
<section class="sign mask">
  <h2 class="headline">Face<br>Mask<br>Required</h2>
  <div class="art-circle" role="img" aria-label="Illustration of a guest wearing a face mask"></div>
  <div class="brand">pine hollow inn</div>
</section>

</body>
</html>
```